RW dental business card. A family dental practice.

Logo plus the following details.

RW Dental
Dr. Marcus Ellory D.D.S
Family. Implant.Cosmetic

48 Fernbrook Lane, Unit 12-13
Markham, ON K2P7R4

Tel: 905-318-2670
Fx:905-318-9025
rwdental-sample.ca

On the double side:

Next app: ______________________

Please notify us at least 48hours in advance to avoid cancellation fees.

Target Market(s)

Family Dental Services

Industry/Entity Type

Dental

Contact Information for Business Card

Put logo prominently and all the info along with it.

Font styles to use
Other font styles liked:
• See Logo Font

Colors
0255a3
3277b5
85acd3
00a990
33b8a4

Requirements
Must have
• Logo and the info stated above.
• See the logo color scheme.
• Or a grayscale (Black, white gray) combination
Nice to have
• A modern unique layout
Should not have
• too simple a design

```html
<!DOCTYPE html>
<html lang="en">
<head>
<meta charset="utf-8">
<title>RW Dental – Business Card</title>
<link href="https://fonts.googleapis.com/css2?family=Open+Sans:wght@400;600;700&display=swap" rel="stylesheet">
<style>
  :root {
    --navy: #013f7c;
    --navy-deep: #0a3a78;
    --teal: #00b9b0;
    --white: #ffffff;
    --backdrop: #eceff2;
    --ink: #1d4f8c;
  }
  * { margin: 0; padding: 0; box-sizing: border-box; }
  html, body { width: 1000px; height: 1200px; overflow: hidden; }
  body {
    background: var(--backdrop);
    font-family: "Open Sans", sans-serif;
    position: relative;
  }
  .card {
    position: absolute;
    left: 107px;
    width: 786px;
    overflow: hidden;
    background: var(--white);
    box-shadow: 0 2px 6px rgba(0,0,0,0.15);
  }

  /* Front */
  .card-front { top: 104px; height: 463px; background: var(--navy); }
  .front-top-band { position: absolute; left: 0; top: 0; width: 100%; height: 149px; background: var(--teal); }
  .front-name-band { position: absolute; left: 0; top: 149px; width: 100%; height: 94px; background: var(--white); }
  .front-emblem { position: absolute; left: -26px; top: 28px; width: 340px; height: 340px; }
  .emblem-name {
    position: absolute; left: 36px; top: 179px; width: 216px;
    text-align: center; color: var(--navy); font-weight: 600; font-size: 32px; line-height: 1.1;
  }
  .doctor-name {
    position: absolute; right: 89px; top: 70px;
    color: var(--white); font-weight: 600; font-size: 21px; white-space: nowrap;
  }
  .services {
    position: absolute; right: 89px; top: 104px;
    color: var(--white); font-size: 20px; white-space: nowrap;
  }
  .practice-name {
    position: absolute; left: 322px; top: 152px;
    color: var(--teal); font-weight: 400; font-size: 48px; line-height: 1.1; white-space: nowrap;
  }
  .tagline {
    position: absolute; left: 324px; top: 211px;
    color: var(--navy); font-size: 16.5px; white-space: nowrap;
  }
  .contact-list { position: absolute; left: 436px; top: 258px; list-style: none; color: var(--white); font-size: 19.5px; line-height: 1.35; }
  .contact-item { display: flex; align-items: flex-start; margin-bottom: 6px; }
  .contact-item svg { width: 24px; height: 24px; margin-right: 9px; margin-top: 3px; flex: none; }
  .contact-item.address { margin-bottom: 10px; }

  /* Back */
  .card-back { top: 649px; height: 472px; }
  .back-band { position: absolute; left: 0; top: 0; width: 100%; height: 111px; background: var(--teal); }
  .back-emblem { position: absolute; left: 36px; top: 12px; width: 150px; height: 150px; }
  .back-emblem-name {
    position: absolute; left: 46px; top: 73px; width: 130px;
    text-align: center; color: var(--navy); font-weight: 600; font-size: 20px;
  }
  .appointment-title {
    position: absolute; left: 340px; top: 64px;
    color: var(--white); font-weight: 700; font-size: 24px;
  }
  .appointment-lines { position: absolute; left: 186px; top: 140px; width: 513px; }
  .appointment-line { display: flex; align-items: flex-end; height: 52px; color: var(--ink); font-size: 16.5px; }
  .appointment-line .blank { flex: 1; border-bottom: 1.5px solid var(--ink); margin-left: 6px; margin-bottom: 6px; }
  .appointment-line.short .blank { margin-right: 9px; }
  .notice {
    position: absolute; left: 0; width: 100%; top: 406px;
    text-align: center; color: var(--navy-deep); font-size: 20px;
  }
</style>
</head>
<body>

  <section class="card card-front">
    <div class="front-top-band"></div>
    <div class="front-name-band"></div>

    <svg class="front-emblem" viewBox="0 0 340 340" aria-hidden="true">
      <circle cx="170" cy="170" r="154" fill="var(--white)"/>
      <path d="M 12 200 A 160 160 0 0 1 300 78" fill="none" stroke="var(--navy)" stroke-width="8"/>
      <path d="M 329 150 A 160 160 0 0 1 40 262" fill="none" stroke="var(--teal)" stroke-width="8"/>
    </svg>
    <div class="emblem-name">RW Dental</div>

    <div class="doctor-name">DR. Marcus Ellory D.D.S.</div>
    <div class="services">Family. Implant. Cosmetic</div>

    <div class="practice-name">RW Dental</div>
    <div class="tagline">Your dental health support Team</div>

    <ul class="contact-list">
      <li class="contact-item address">
        <svg viewBox="0 0 24 24" aria-hidden="true"><path d="M2 10 L12 4 L22 10 Z" fill="#fff"/><rect x="4" y="10" width="16" height="10" fill="none" stroke="#fff" stroke-width="2"/><rect x="10" y="13" width="4" height="7" fill="#fff"/></svg>
        <span>48 Fernbrook Lane, Unit 12-13<br>Markham, ON K2P7R4</span>
      </li>
      <li class="contact-item">
        <svg viewBox="0 0 24 24" aria-hidden="true"><path d="M6 3 L9 3 L10.5 8 L8.5 10 C9.5 12.5 11.5 14.5 14 15.5 L16 13.5 L21 15 L21 18 C21 19.5 19.5 21 18 21 C10 20 4 14 3 6 C3 4.5 4.5 3 6 3 Z" fill="#fff"/></svg>
        <span>905-318-2670</span>
      </li>
      <li class="contact-item">
        <svg viewBox="0 0 24 24" aria-hidden="true"><rect x="6" y="3" width="12" height="7" fill="none" stroke="#fff" stroke-width="2"/><rect x="3" y="10" width="18" height="10" rx="1" fill="#fff"/><rect x="7" y="15" width="10" height="2" fill="var(--navy)"/></svg>
        <span>905-318-9025</span>
      </li>
      <li class="contact-item">
        <svg viewBox="0 0 24 24" aria-hidden="true"><circle cx="12" cy="12" r="9" fill="none" stroke="#fff" stroke-width="1.8"/><ellipse cx="12" cy="12" rx="4" ry="9" fill="none" stroke="#fff" stroke-width="1.5"/><line x1="3" y1="12" x2="21" y2="12" stroke="#fff" stroke-width="1.5"/><line x1="12" y1="3" x2="12" y2="21" stroke="#fff" stroke-width="1.5"/></svg>
        <span>www.rwdental-sample.ca</span>
      </li>
    </ul>
  </section>

  <section class="card card-back">
    <div class="back-band"></div>
    <svg class="back-emblem" viewBox="0 0 150 150" aria-hidden="true">
      <circle cx="75" cy="75" r="72" fill="var(--white)"/>
      <path d="M 138 70 A 62 62 0 0 1 20 100" fill="none" stroke="var(--teal)" stroke-width="5"/>
    </svg>
    <div class="back-emblem-name">RW Dental</div>

    <div class="appointment-title">Appointment:</div>

    <div class="appointment-lines">
      <div class="appointment-line short"><span>Date</span><span class="blank"></span></div>
      <div class="appointment-line"><span>Time</span><span class="blank"></span></div>
      <div class="appointment-line short"><span>Date</span><span class="blank"></span></div>
      <div class="appointment-line"><span>Time</span><span class="blank"></span></div>
    </div>

    <p class="notice">Please notify us at least 48hours in advance to avoid cancellation fees.</p>
  </section>

</body>
</html>
```